Kettle Past Noon - Book cover for collection of odd short stories

We need a book cover for ebook and print versions for an anthology of short stories. The title "Kettle Past Noon" relates to stories with something odd or not-quite-right about them. The attached photo is an example of a carpenter level, the idea is the level would appear perfectly level, but the bubble would be off-center. "Stories by: Moira Tesslund, Janet Orloff, Rob T. Vessey, Author, Author". Other creative elements could be wildly improbable things, e.g. pig's flying, hell freezing, etc. We prefer an uncluttered cover, however. Licenses included or unnecessary, delivery files must be fully compatible with Adobe Illustrator, with all layers intact.

Target Market(s)

People who like short stories with odd overtones or twist endings.

Industry/Entity Type

Book Publisher

Font styles to use
Serif

Colors

Designer to choose colors to be used in the design.

Requirements
Must have
• Incorporation of the concept, Kettle Past Noon
Nice to have
• Other ways to show the same meaning

```html
<!DOCTYPE html>
<html lang="en">
<head>
<meta charset="utf-8">
<title>Kettle Past Noon – Book Cover</title>
<link rel="stylesheet" href="https://fonts.googleapis.com/css2?family=Pathway+Gothic+One&family=Libre+Baskerville&display=swap">
<style>
  :root {
    --backdrop: #bdbdbd;
    --cover: #1e1b18;
    --title-light: #e8eef7;
    --title-red: #c21d1f;
    --connector-grey: #8a8a8a;
    --author-white: #f2f0ec;
    --art-top: #1e1b18;
    --art-mid: #33424d;
    --art-low: #8a4a5c;
  }
  html, body {
    margin: 0;
    padding: 0;
    width: 1200px;
    height: 1200px;
    overflow: hidden;
    background: var(--backdrop);
  }
  .book-cover {
    position: absolute;
    left: 264px;
    top: 95px;
    width: 674px;
    height: 1010px;
    background: var(--cover);
    overflow: hidden;
  }
  .title {
    margin: 0;
    font-family: "Pathway Gothic One", "Arial Narrow", sans-serif;
    font-weight: 400;
  }
  .title span {
    position: absolute;
    left: 0;
    width: 100%;
    text-align: center;
    line-height: 1;
    z-index: 2;
  }
  .title-top {
    top: 35px;
    font-size: 197px;
    color: var(--title-light);
  }
  .title-connector {
    top: 226px;
    font-size: 50px;
    color: var(--connector-grey);
  }
  .title-bottom {
    top: 249px;
    font-size: 175px;
    color: var(--title-red);
  }
  .cover-art {
    position: absolute;
    left: 261px;
    top: 400px;
    width: 156px;
    height: 610px;
    background: linear-gradient(to bottom, var(--art-top) 0%, var(--art-mid) 30%, var(--art-mid) 55%, var(--art-low) 75%, var(--art-top) 100%);
    z-index: 1;
  }
  .authors {
    position: absolute;
    left: 0;
    top: 903px;
    width: 100%;
    margin: 0;
    text-align: center;
    font-family: "Libre Baskerville", Georgia, serif;
    font-size: 19px;
    letter-spacing: 2px;
    line-height: 30px;
    text-transform: uppercase;
    color: var(--author-white);
    z-index: 3;
  }
</style>
</head>
<body>
  <main class="book-cover">
    <h1 class="title">
      <span class="title-top">Kettle</span>
      <span class="title-connector">past</span>
      <span class="title-bottom">Noon</span>
    </h1>
    <div class="cover-art" role="img" aria-label="Photograph of a burning match with a blue and red flame rising from its head"></div>
    <p class="authors">Moira Tesslund, Janet Orloff,<br>Rob T. Vessey, Author, Author</p>
  </main>
</body>
</html>
```